Need a website for our company

We need a website for our company to showcase all our work for customers to see.
We do all phases of home improvement:
Dormers/Extensions
Basement Remodel
Masonry/Concrete/Pavers/Asphalt
Cultured Stone Veneer
Kitchens
Bathrooms
Pool designs
Outdoor Bathroom
Outdoor Kitchens
Tile work
For reference, something similar to this website: https://brightlanebuilders.example/
Target Market(s)
We are trying to target homeowners.
Coding
Coded - Design and coding required
Number of Pages Required
5+ page
Look and feel

```html
<!DOCTYPE html>
<html lang="en">
<head>
<meta charset="utf-8">
<title>Harlow &amp; Sons Construction Inc</title>
<link href="https://fonts.googleapis.com/css2?family=Montserrat:wght@400;500;600;700;800;900&display=swap" rel="stylesheet">
<style>
:root{
  --orange:#e8401c;
  --ink:#1b1b1b;
  --text:#3c3c3c;
  --muted:#8a8a8a;
  --band:#f1eff0;
  --dark:#262626;
  --black:#0b0b0b;
  --white:#ffffff;
}
*{margin:0;padding:0;box-sizing:border-box}
html,body{width:1200px;height:4164px;overflow:hidden}
body{position:relative;background:var(--white);font-family:"Montserrat",sans-serif;color:var(--text)}
.abs{position:absolute}
.photo{position:absolute;display:block}
.btn{position:absolute;background:var(--orange);color:var(--white);font-weight:700;text-transform:uppercase;display:flex;align-items:center;justify-content:center;letter-spacing:.3px}
.section-title{position:absolute;left:0;width:1200px;text-align:center;font-weight:900;font-size:20px;color:var(--ink);text-transform:uppercase;letter-spacing:-.3px}
.title-rule{position:absolute;left:586px;width:28px;height:2px;background:var(--ink)}

/* header */
.brand{left:131px;top:16px;width:180px;text-align:center}
.brand-mark{width:14px;height:14px;border:3px solid #444;margin:8px auto 10px}
.brand-name{font-size:10px;font-weight:700;color:#555;letter-spacing:.6px}
.brand-tag{font-size:6px;color:#888;letter-spacing:1.2px;margin-top:3px;line-height:1.3}
.quote-top{left:681px;top:0;width:158px;height:60px;font-size:14px}
.call{left:839px;top:0;width:227px;height:60px;background:var(--dark);color:var(--white)}
.call svg{position:absolute;left:18px;top:16px}
.call-small{position:absolute;left:60px;top:12px;font-size:10px;font-weight:500}
.call-big{position:absolute;left:60px;top:26px;font-size:18px;font-weight:600}
.nav{top:82px;left:603px;display:flex;gap:0;font-size:13px;font-weight:600;color:var(--ink)}
.nav a{position:absolute;white-space:nowrap;text-decoration:none;color:var(--ink)}
.nav a.active{color:var(--orange)}
.nav a.active::after{content:"";position:absolute;left:0;right:0;bottom:-8px;height:2px;background:var(--orange)}

/* hero */
.hero{left:0;top:120px;width:1200px;height:583px;background:linear-gradient(180deg,#8e8478 0%,#b9aa97 40%,#9a7856 75%,#7a5a3e 100%)}
.hero-title{top:312px;left:0;width:1200px;text-align:center;color:var(--white);font-weight:900;font-size:36px;letter-spacing:-1px;text-shadow:0 2px 6px rgba(0,0,0,.35)}
.hero-btn{left:506px;top:378px;width:188px;height:52px;font-size:18px}
.dots{left:562px;top:654px;display:flex;gap:9px}
.dots i{width:8px;height:8px;border-radius:50%;background:var(--white);display:block}
.dots i.on{background:var(--orange)}

/* services */
.card-img{width:293px;height:210px}
.card-title{position:absolute;width:293px;text-align:center;font-size:15px;font-weight:700;color:var(--ink)}
.card-desc{position:absolute;width:293px;text-align:center;font-size:12px;line-height:16px;color:var(--text)}
.card-btn{width:95px;height:28px;font-size:11px}
.outline-btn{left:506px;top:1593px;width:189px;height:39px;border:2px solid var(--orange);color:var(--orange);font-weight:700;font-size:14px;display:flex;align-items:center;justify-content:center}

/* welcome */
.welcome-band{left:0;top:1714px;width:1200px;height:379px;background:var(--band)}
.welcome-title{left:131px;top:1750px;font-size:20px;font-weight:900;color:var(--ink);letter-spacing:-.3px}
.welcome-rule{left:131px;top:1790px;width:28px;height:2px;background:var(--ink)}
.welcome-text{left:131px;top:1824px;width:424px;font-size:12px;line-height:19px;text-align:justify}
.welcome-btn{left:131px;top:2026px;width:96px;height:28px;font-size:11px}

/* testimonials */
.t-card{position:absolute;top:2269px;width:295px;height:351px;background:var(--white);box-shadow:0 2px 14px rgba(0,0,0,.08);text-align:center}
.t-quote{margin-top:26px;font-size:30px;font-weight:800;color:var(--ink);line-height:30px}
.t-text{margin:10px auto 0;width:210px;font-size:12px;line-height:19.5px;color:var(--text)}
.t-stars{margin-top:18px;color:var(--orange);font-size:12px;letter-spacing:1px}
.t-name{margin-top:8px;font-size:11px;font-weight:700;color:var(--ink)}
.arrow{position:absolute}

/* work */
.work-band{left:0;top:2692px;width:1200px;height:647px;background:var(--band)}
.work-label{position:absolute;top:3188px;font-size:18px;font-weight:500;color:var(--white)}
.work-btn{left:532px;top:3268px;width:136px;height:29px;font-size:11px}

/* contact */
.contact{left:0;top:3339px;width:1200px;height:490px;background:linear-gradient(180deg,#3a3633 0%,#2a2826 60%,#1f1d1b 100%)}
.contact-title{color:var(--white)}
.field{position:absolute;background:var(--white);font-size:12px;color:#555;padding:16px 20px}
.submit{left:551px;top:3740px;width:98px;height:34px;font-size:14px}

/* footer */
.footer{left:0;top:3829px;width:1200px;height:335px;background:var(--black);color:var(--white)}
.f-brand{left:131px;top:3930px;width:262px;text-align:center}
.f-brand .brand-mark{width:22px;height:22px;border-color:#777;margin-bottom:22px}
.f-brand .brand-name{color:#9a9a9a;font-size:12px;letter-spacing:1.4px}
.f-brand .brand-tag{color:#777;font-size:8px}
.f-head{position:absolute;top:3862px;font-size:12px;font-weight:700;color:var(--white)}
.f-line{position:absolute;top:3886px;height:2px;background:#cfcfcf}
.f-item{position:absolute;font-size:11px;line-height:16px;color:#e6e6e6}
.f-icon{position:absolute;width:22px;height:22px;border-radius:50%;background:var(--white)}
.f-menu{position:absolute;left:708px;top:3916px;font-size:11px;line-height:24px;color:#e6e6e6}
.f-rule{left:131px;top:4091px;width:938px;height:1px;background:#333}
.copyright{left:0;top:4121px;width:1200px;text-align:center;font-size:11px;color:#ddd}
</style>
</head>
<body>

<!-- header -->
<div class="abs brand">
  <div class="brand-mark"></div>
  <div class="brand-name">HARLOW &amp; SONS CONSTRUCTION INC</div>
  <div class="brand-tag">WE TREAT OUR CUSTOMERS LIKE FAMILY<br>'LA FAMIGLIA'</div>
</div>
<div class="btn quote-top">Get a Quote</div>
<div class="abs call">
  <svg width="30" height="30" viewBox="0 0 30 30"><circle cx="15" cy="15" r="13" fill="none" stroke="#fff" stroke-width="1.6"/><path d="M10 9c1-1 2 0 3 2s0 2-1 3c1 2 2 3 4 4 1-1 1-2 3-1s3 2 2 3c-2 2-5 2-9-2s-4-7-2-9z" fill="#fff"/></svg>
  <div class="call-small">Call Us Today</div>
  <div class="call-big">+1 555 0100 2200</div>
</div>
<nav class="abs nav" style="left:0;width:1200px">
  <a class="active" style="left:603px">HOME</a>
  <a style="left:679px">ABOUT</a>
  <a style="left:767px">SERVICES</a>
  <a style="left:868px">OUR WORK</a>
  <a style="left:978px">CONTACT US</a>
</nav>

<!-- hero -->
<div class="abs hero" role="img" aria-label="Bright modern kitchen with white cabinets, marble island, bar stools and pendant lights"></div>
<div class="abs hero-title">WE TREAT OUR CUSTOMERS LIKE FAMILY</div>
<div class="btn hero-btn">Get a Quote</div>
<div class="abs dots"><i></i><i></i><i class="on"></i><i></i><i></i></div>

<!-- services -->
<div class="section-title" style="top:740px">Our Services</div>
<div class="title-rule" style="top:780px"></div>

<div class="photo card-img" style="left:133px;top:817px;background:linear-gradient(180deg,#6f9ad0,#9b4a44 60%,#6e6a60)" role="img" aria-label="House with red dormers"></div>
<div class="card-title" style="left:133px;top:1049px">Dormers / Extensions</div>
<div class="card-desc" style="left:133px;top:1080px">Transform your home with stunning<br>dormers and extensions today</div>
<div class="btn card-btn" style="left:231px;top:1130px">Read More</div>

<div class="photo card-img" style="left:454px;top:817px;background:linear-gradient(180deg,#d9d6d0,#9e9a94 60%,#7c7974)" role="img" aria-label="Finished basement with fireplace and carpet"></div>
<div class="card-title" style="left:454px;top:1049px">Basement Remodel</div>
<div class="card-desc" style="left:454px;top:1080px">Unlock the potential of your basement<br>with stunning remodel.</div>
<div class="btn card-btn" style="left:553px;top:1130px">Read More</div>

<div class="photo card-img" style="left:773px;top:817px;background:linear-gradient(135deg,#6a5a4e,#9c8a7c 50%,#4d4540)" role="img" aria-label="Hand smoothing wet concrete"></div>
<div class="card-title" style="left:773px;top:1049px">Masonry/Concrete/Pavers/Asphalt</div>
<div class="card-desc" style="left:773px;top:1080px">Enhance your property with durable<br>masonry, concrete, pavers, asphalt.</div>
<div class="btn card-btn" style="left:871px;top:1130px">Read More</div>

<div class="photo card-img" style="left:133px;top:1195px;background:linear-gradient(180deg,#e9e9e7,#c9c4ba 60%,#a99a82)" role="img" aria-label="White kitchen with wooden island"></div>
<div class="card-title" style="left:133px;top:1427px">Kitchens</div>
<div class="card-desc" style="left:133px;top:1458px">Upgrade your home and increase its value<br>with stunning kitchens.</div>
<div class="btn card-btn" style="left:231px;top:1509px">Read More</div>

<div class="photo card-img" style="left:454px;top:1195px;background:linear-gradient(90deg,#e6e2db,#c8b9a4 55%,#8f8a82)" role="img" aria-label="Modern bathroom with tiled walls"></div>
<div class="card-title" style="left:454px;top:1427px">Bathrooms</div>
<div class="card-desc" style="left:454px;top:1458px">Experience the ultimate relaxation with<br>stunning and functional bathrooms.</div>
<div class="btn card-btn" style="left:553px;top:1509px">Read More</div>

<div class="photo card-img" style="left:773px;top:1195px;background:linear-gradient(180deg,#cfe0ef,#e9e7e2 45%,#3fa9b8 75%,#2a7f8c)" role="img" aria-label="Outdoor pool beside modern house"></div>
<div class="card-title" style="left:773px;top:1427px">Pool designs</div>
<div class="card-desc" style="left:773px;top:1458px">Dive into luxury and relaxation with<br>breathtaking pool designs.</div>
<div class="btn card-btn" style="left:871px;top:1509px">Read More</div>

<div class="abs outline-btn">VIEW ALL SERVICES</div>

<!-- welcome -->
<div class="abs welcome-band"></div>
<div class="abs welcome-title">WELCOME TO HARLOW &amp; SONS</div>
<div class="abs welcome-rule"></div>
<p class="abs welcome-text">It is a long established fact that a reader will be distracted by the readable content of a page when looking at its layout. The point of using Lorem Ipsum is that it has a more-or-less normal distribution of letters, as opposed to using 'Content here, content here', making it look like readable English. Many desktop publishing packages and web page editors now use Lorem Ipsum as their default model text, and a search for 'lorem ipsum' will uncover many web sites still in their infancy. Various versions have evolved over the years, sometimes by accident, sometimes on purpose (injected humour and the like).</p>
<div class="btn welcome-btn">Read More</div>
<div class="photo" style="left:602px;top:1687px;width:224px;height:271px;background:linear-gradient(135deg,#8a7f6c,#b3a58a 50%,#6a6052)" role="img" aria-label="Cultured stone veneer wall"></div>
<div class="photo" style="left:843px;top:1687px;width:223px;height:148px;background:linear-gradient(135deg,#d8c8ae,#ece2d0 55%,#bfa98a)" role="img" aria-label="Hands laying travertine tiles"></div>
<div class="photo" style="left:603px;top:1971px;width:223px;height:152px;background:linear-gradient(135deg,#4a4440,#a97a55 50%,#d6c2a6)" role="img" aria-label="Tile samples held against a wall"></div>
<div class="photo" style="left:843px;top:1848px;width:223px;height:272px;background:linear-gradient(180deg,#4f8fd0,#5e7a4c 35%,#8a8478 70%,#6a6660)" role="img" aria-label="Outdoor stone kitchen with grill"></div>

<!-- testimonials -->
<div class="section-title" style="top:2181px">Testimonials</div>
<div class="title-rule" style="top:2221px"></div>
<svg class="arrow" style="left:66px;top:2422px" width="16" height="28" viewBox="0 0 16 28"><path d="M14 2 3 14l11 12" fill="none" stroke="#999" stroke-width="2"/></svg>
<svg class="arrow" style="left:1112px;top:2422px" width="16" height="28" viewBox="0 0 16 28"><path d="M2 2l11 12L2 26" fill="none" stroke="#999" stroke-width="2"/></svg>

<div class="t-card" style="left:133px">
  <div class="t-quote">“</div>
  <p class="t-text">It is a long established fact that a reader will be distracted by the readable content of a page when looking at its layout. The point of using Lorem Ipsum is that it has a more-or-less normal distribution of letters, as opposed to using 'Content here, content here', making it look like readable English. Many</p>
  <div class="t-stars">★★★★★</div>
  <div class="t-name">DANIEL</div>
</div>
<div class="t-card" style="left:453px">
  <div class="t-quote">“</div>
  <p class="t-text">It is a long established fact that a reader will be distracted by the readable content of a page when looking at its layout. The point of using Lorem Ipsum is that it has a more-or-less normal distribution of letters, as opposed to using 'Content here, content here', making it look like readable English. Many</p>
  <div class="t-stars">★★★★★</div>
  <div class="t-name">DANIEL</div>
</div>
<div class="t-card" style="left:773px">
  <div class="t-quote">“</div>
  <p class="t-text">It is a long established fact that a reader will be distracted by the readable content of a page when looking at its layout. The point of using Lorem Ipsum is that it has a more-or-less normal distribution of letters, as opposed to using 'Content here, content here', making it look like readable English. Many</p>
  <div class="t-stars">★★★★★</div>
  <div class="t-name">DANIEL</div>
</div>

<!-- our work -->
<div class="abs work-band"></div>
<div class="section-title" style="top:2733px">Our Work</div>
<div class="title-rule" style="top:2773px"></div>
<svg class="arrow" style="left:62px;top:3004px" width="16" height="28" viewBox="0 0 16 28"><path d="M14 2 3 14l11 12" fill="none" stroke="#999" stroke-width="2"/></svg>
<svg class="arrow" style="left:1106px;top:3004px" width="16" height="28" viewBox="0 0 16 28"><path d="M2 2l11 12L2 26" fill="none" stroke="#999" stroke-width="2"/></svg>
<div class="photo" style="left:133px;top:2811px;width:307px;height:417px;background:linear-gradient(180deg,#d9d2c4,#b8ab94 45%,#e8e6e1 65%,#1e2a3c)" role="img" aria-label="Kitchen with gold chandeliers and navy island"></div>
<div class="photo" style="left:440px;top:2811px;width:314px;height:417px;background:linear-gradient(180deg,#cfcac4,#a39d96 50%,#4a4642)" role="img" aria-label="Modern bathroom with walk-in shower"></div>
<div class="photo" style="left:754px;top:2811px;width:312px;height:417px;background:linear-gradient(180deg,#9fb8cf,#5d6d5a 45%,#3f9dbf 75%,#2a6f8a)" role="img" aria-label="Backyard pool under large trees"></div>
<div class="work-label" style="left:155px">Kitchen</div>
<div class="work-label" style="left:459px">Bathroom</div>
<div class="work-label" style="left:786px">Pool designs</div>
<div class="btn work-btn">View All Works</div>

<!-- contact -->
<div class="abs contact" role="img" aria-label="Dim backyard patio with outdoor furniture behind the form"></div>
<div class="section-title contact-title" style="top:3384px">Contact Us</div>
<div class="title-rule" style="top:3424px;background:var(--white)"></div>
<div class="field" style="left:267px;top:3470px;width:327px;height:44px;padding-top:15px">First Name</div>
<div class="field" style="left:608px;top:3470px;width:327px;height:44px;padding-top:15px">Last Name</div>
<div class="field" style="left:267px;top:3532px;width:327px;height:43px;padding-top:15px">Email id</div>
<div class="field" style="left:608px;top:3532px;width:327px;height:43px;padding-top:15px">Phone</div>
<div class="field" style="left:267px;top:3593px;width:671px;height:113px">Message</div>
<div class="btn submit">Submit</div>

<!-- footer -->
<div class="abs footer"></div>
<div class="abs brand f-brand">
  <div class="brand-mark"></div>
  <div class="brand-name">HARLOW &amp; SONS CONSTRUCTION INC</div>
  <div class="brand-tag">WE TREAT OUR CUSTOMERS LIKE FAMILY<br>'LA FAMIGLIA'</div>
</div>

<div class="f-head" style="left:422px">CONTACT US</div>
<div class="f-line" style="left:422px;width:193px"></div>
<svg class="abs" style="left:422px;top:3920px" width="22" height="22" viewBox="0 0 22 22"><circle cx="11" cy="11" r="11" fill="#fff"/><path d="M11 5a4 4 0 0 1 4 4c0 3-4 8-4 8s-4-5-4-8a4 4 0 0 1 4-4z" fill="#111"/><circle cx="11" cy="9" r="1.5" fill="#fff"/></svg>
<div class="f-item" style="left:456px;top:3917px">742 Maple Ridge Road<br>Suite 210, Springfield, GA 30000</div>
<svg class="abs" style="left:422px;top:3968px" width="22" height="22" viewBox="0 0 22 22"><circle cx="11" cy="11" r="11" fill="#fff"/><path d="M7 6c1-1 2 0 3 2s0 2-1 3c1 2 2 3 4 4 1-1 1-2 3-1s2 2 1 3c-2 2-5 1-8-2s-3-7-2-9z" fill="#111"/></svg>
<div class="f-item" style="left:456px;top:3965px">Call Us<br>+1 555 010 2200</div>
<svg class="abs" style="left:422px;top:4021px" width="22" height="22" viewBox="0 0 22 22"><circle cx="11" cy="11" r="11" fill="#fff"/><rect x="5.5" y="7" width="11" height="8" fill="none" stroke="#111" stroke-width="1.4"/><path d="M5.5 7l5.5 4.5L16.5 7" fill="none" stroke="#111" stroke-width="1.4"/></svg>
<div class="f-item" style="left:456px;top:4018px">E mail Us<br>info@harlowsons.example</div>

<div class="f-head" style="left:708px">MENU</div>
<div class="f-line" style="left:708px;width:106px"></div>
<div class="f-menu">HOME<br>ABOUT<br>SERVICES<br>OUR WORK<br>CONTACT US</div>

<div class="f-head" style="left:925px">FOLLOW US</div>
<div class="f-line" style="left:925px;width:108px"></div>
<div class="f-icon" style="left:925px;top:3921px"></div>
<div class="f-item" style="left:960px;top:3917px">Like us on<br>COMMUNITY PAGE</div>
<div class="f-icon" style="left:925px;top:3971px"></div>
<div class="f-item" style="left:960px;top:3967px">Follow us on<br>NEWS FEED</div>
<div class="f-icon" style="left:925px;top:4022px"></div>
<div class="f-item" style="left:960px;top:4018px">Follow us on<br>PRO NETWORK</div>

<div class="abs f-rule"></div>
<div class="abs copyright">Copyright © 2023 All Rights Reserved</div>

</body>
</html>
```